依頼詳細
ポスティング形式での営業となりますので、
一目見て目に付くようなチラシデザインで
あれば、多少デザインに派手さが入っても
良いとは思っています。

「本当に和室のままでイイですか?」
というアラートの様なタイトルがどれだけ
目を引くかに重点を置いて考えています。

また、何故和室を洋室に変えた方がイイと
いう根拠につきましては、
・畳の経年寿命の早さとメンテナンス&交換をしてない畳のアレルギー等の促進を
進めるという情報をわかりやすくアラートをお伝えした文章が欲しいです。(ハウスダスト・ダニ・花粉)

価格帯の記載
・マンションアパートタイプであれば
1畳単価50000円〜
・戸建てタイプの場合い1畳単価60000円〜
押し入れのクローゼット化 10000円〜

室内の物の移動等も含める作業は別途
お見積もりとの別記載も入れて欲しい。

和室〜洋室に変えた際のビフォーアフターの
写真等も添付したいです。
記載項目
翠昇株式会社 03-6812-3097
HP https://suishoweb.ne.jp/
キャッチコピー「和室のままで本当にイイですか?」
サイズ
A4
ページ数
両面
希望イメージ
シンプル 複雑
単色 カラフル
暗い 明るい
日常 高級
遊び心 厳粛
未来的 伝統的
女性的 男性的
希望する色
青系
納品ファイル
• 高解像度JPG (.jpg)
• PNG形式 (.png)
補足説明
デザイン 文章 画像についても提案があれば都度頂きたい。
■ 選んだ理由

シンプルで有りながらも、ディテールの部分の丁寧さがスゴく見やすく思えました。文章につきましても
拙い説明にも関わらず、しっかり拾い上げて頂けたのが1番決め手となりました。本当にありがとうございます。

■ 提案者全員のお礼・コメント

この度は沢山のご提案頂きありがとうございました。
タスクフォルンを使ったのは初めてで、色々分からず皆様に失礼が有りましたらここでお詫びさせて下さい。

とてもタスクフォルンのサービスとデザイナーの皆様の
技術に大変関心を持ちました。今後も色んな事で
運用したいと思っておりますので、また機会が
ございましたら何卒よろしくお願い致します。

この度は誠に有難うございました。

```html
<!DOCTYPE html>
<html lang="ja">
<head>
<meta charset="utf-8">
<title>お部屋リフォームのご案内｜翠昇株式会社</title>
<link rel="stylesheet" href="https://fonts.googleapis.com/css2?family=Noto+Sans+JP:wght@500;700;900&family=Shippori+Mincho:wght@600;800&display=swap">
<style>
  :root {
    --paper: #f1e9db;
    --paper-light: #f8f3ea;
    --ink: #3d3530;
    --accent: #d9742b;
    --arrow-red: #d2452f;
    --footer-brown: #5b4132;
    --tab-brown: #8a5a3a;
    --white: #ffffff;
    --photo-room-a: #d9d4cc;
    --photo-room-b: #bfa888;
    --photo-person-a: #b9c8d8;
    --photo-person-b: #8d98a6;
  }
  * { margin: 0; padding: 0; box-sizing: border-box; }
  html, body { width: 848px; height: 1200px; overflow: hidden; }
  body {
    background: radial-gradient(ellipse at 50% 45%, var(--paper-light) 0%, var(--paper) 70%);
    font-family: "Noto Sans JP", sans-serif;
    color: var(--ink);
    position: relative;
  }
  .flyer { position: absolute; inset: 0; }

  .headline {
    position: absolute;
    writing-mode: vertical-rl;
    font-weight: 900;
    line-height: 1;
    letter-spacing: 0;
    color: var(--ink);
  }
  .headline--right { right: 30px; top: 40px; }
  .headline--right .sm { font-size: 95px; }
  .headline--right .lg {
    font-size: 135px;
    background: linear-gradient(to left, var(--accent) 0 10px, transparent 10px);
    padding-right: 4px;
  }
  .headline--left { left: 35px; top: 60px; }
  .headline--left .lg { font-size: 150px; }
  .headline--left .sm { font-size: 85px; }

  .room-circle {
    position: absolute;
    border-radius: 50%;
    border: 5px solid var(--white);
    box-shadow: 0 2px 6px rgba(0,0,0,.15);
  }
  .room-circle--after {
    left: 254px; top: 56px; width: 160px; height: 160px;
    background: linear-gradient(160deg, var(--paper-light), var(--photo-room-a) 60%, #b8a48c);
  }
  .room-circle--before {
    left: 446px; top: 27px; width: 184px; height: 184px;
    background: linear-gradient(160deg, #e6dccb, var(--photo-room-b) 70%, #8e7656);
  }
  .change-arrow { position: absolute; left: 418px; top: 120px; }

  .person-photo {
    position: absolute;
    left: 270px; top: 255px; width: 370px; height: 765px;
    background: linear-gradient(180deg, transparent 0%, var(--photo-person-a) 20%, var(--photo-person-a) 65%, var(--photo-person-b) 100%);
    border-radius: 150px 150px 0 0;
    opacity: .9;
  }

  .message-box {
    position: absolute;
    left: 310px; top: 850px; width: 400px; height: 125px;
    background: rgba(255,255,255,.94);
    text-align: center;
    padding-top: 22px;
    box-shadow: 0 2px 8px rgba(0,0,0,.1);
  }
  .message-box__lead { font-size: 30px; font-weight: 700; letter-spacing: 2px; }
  .message-box__sub { font-size: 27px; font-weight: 700; margin-top: 8px; letter-spacing: 1px; }
  .message-box__sub em { font-style: normal; color: var(--accent); }

  .footer {
    position: absolute;
    left: 0; right: 0; bottom: 0; height: 180px;
    background: var(--footer-brown);
    color: var(--white);
    text-align: center;
    padding-top: 40px;
  }
  .footer__company {
    font-family: "Shippori Mincho", serif;
    font-weight: 800;
    font-size: 38px;
    letter-spacing: 6px;
  }
  .footer__info { font-size: 14px; font-weight: 500; margin-top: 20px; letter-spacing: .5px; padding-right: 60px; }

  .detail-tab {
    position: absolute;
    right: 0; top: 1005px; width: 72px; height: 170px;
    background: var(--tab-brown);
    color: var(--white);
    display: flex; flex-direction: column; align-items: center;
    padding-top: 12px;
  }
  .detail-tab__text {
    writing-mode: vertical-rl;
    font-size: 19px; font-weight: 700; line-height: 1.15;
  }
  .detail-tab__icon { margin-top: 8px; }
</style>
</head>
<body>
<main class="flyer">
  <div class="room-circle room-circle--after" role="img" aria-label="リフォーム後の洋室の写真"></div>
  <svg class="change-arrow" width="30" height="30" viewBox="0 0 30 30" aria-hidden="true">
    <path d="M20 4 L8 15 L20 26" fill="none" stroke="var(--arrow-red)" stroke-width="3.5"/>
  </svg>
  <div class="room-circle room-circle--before" role="img" aria-label="リフォーム前の和室の写真"></div>

  <div class="person-photo" role="img" aria-label="腕を組んで考え込む年配男性の写真"></div>

  <h1 class="headline headline--right"><span class="sm">今後も</span><span class="lg">和室</span><span class="sm">のままで</span></h1>
  <p class="headline headline--left"><span class="lg">本当</span><span class="sm">にイイですか？</span></p>

  <div class="message-box">
    <p class="message-box__lead">より快適な毎日へ！</p>
    <p class="message-box__sub"><em>お部屋リフォーム</em>のご案内です</p>
  </div>

  <footer class="footer">
    <p class="footer__company">翠昇 株式会社</p>
    <p class="footer__info">〒150-0031 東京都渋谷区桜丘町8-21-3　〈事業内容〉リフォーム・リノベーション工事／住宅工事／オフィス改装</p>
  </footer>

  <div class="detail-tab">
    <span class="detail-tab__text">詳細は<br>裏面へ</span>
    <svg class="detail-tab__icon" width="26" height="26" viewBox="0 0 26 26" aria-hidden="true">
      <circle cx="13" cy="13" r="12" fill="var(--white)"/>
      <path d="M10 7 L16 13 L10 19" fill="none" stroke="var(--tab-brown)" stroke-width="3"/>
    </svg>
  </div>
</main>
</body>
</html>
```